Startup Technology Consulting Firm in NYC Needs A Website

I need a website built for my startup technology consulting company Brightmoor Systems Collective. We offer a unique white glove service that provides end to end technology support. I want to stand out above the rest. We are small firm but are very dedicated which where we derive our name from BSC primarily offers
end to end technology advisory services to small businesses lacking their own IT staff. We offer top notch white glove and our customer service and satisfaction is exceed by no one.

Below are some of what we provide our clients

Strategic IT Planning
Business Continuity Planning/Disaster Recovery
Cloud Computing\DataCenter Solutions
Server Infrastructure/Networking
Virtualization Technologies
Project Management

Our Technology Advisors hold many certifications from Quillora & Tessfold. We are also Quillora Partners

I have attached my logo (preview design) As soon as I ge the final images I will upload.

Reason: want to give more time to submit designs

Industry/Entity Type

Information Technology

Coding

Coded - Design and coding required

Number of Pages Required

1 page

Font styles to use
Sans Serif

Requirements
Must have
• Attract Target Market. The site should bleed the company vision
• DEDICATION everything about the site should show this
• Layout the Benefits of our offerings
• Links to my social media
• Links to dircct my client's for remote support

```html
<!DOCTYPE html>
<html lang="en">
<head>
<meta charset="utf-8">
<title>Brightmoor Systems Collective</title>
<link href="https://fonts.googleapis.com/css2?family=Open+Sans:wght@300;400;600&family=Roboto+Condensed:wght@700&display=swap" rel="stylesheet">
<style>
  :root{
    --blue:#0b63b0;
    --blue-text:#1d6db5;
    --ink:#1c1c1c;
    --body:#333;
    --green:#7fbd32;
    --green-dark:#5f9a1d;
    --vision-bg:#dcedfb;
    --vision-edge:#b3d1ea;
  }
  *{box-sizing:border-box;margin:0;padding:0}
  a{text-decoration:none;color:inherit}
  html,body{width:1200px;height:1200px;overflow:hidden;background:#fff}
  body{font-family:"Open Sans",sans-serif;color:var(--body);position:relative}

  .site-header{position:absolute;left:0;top:0;width:1200px;height:127px;
    background:linear-gradient(90deg,#f4f6f8,#eef2f5 60%,#e9eef2)}
  .brand{position:absolute;left:52px;top:30px;display:flex;align-items:center;gap:12px}
  .brand-mark{width:44px;height:44px;border-radius:50%;background:#dbe8f4}
  .brand-name{font-size:21px;font-weight:600;color:var(--blue);line-height:1.15;width:190px}
  .call{position:absolute;right:64px;top:10px;font-size:15px;color:#333}
  .call strong{color:var(--blue);font-weight:600;font-size:17px}
  .social{position:absolute;top:45px;left:996px;display:flex;gap:6px}
  .social a{display:block;width:40px;height:40px;border-radius:50%;border:1.5px solid #4a6ea8}
  .social a.second{border-color:#2d9ad6}
  .social a.third{border-color:#d9534f}
  .nav{position:absolute;top:97px;left:0;width:1200px;font-size:15px;color:#222}
  .nav a{position:absolute;padding-bottom:8px}
  .nav a.active{color:var(--blue-text);border-bottom:2px solid var(--blue-text)}

  .hero{position:absolute;left:0;top:127px;width:1200px;height:506px;overflow:hidden;
    background:
      radial-gradient(ellipse 420px 320px at 180px 320px,#eaf3f2 0%,rgba(234,243,242,0) 70%),
      radial-gradient(ellipse 260px 220px at 640px 330px,#c9b5aa 0%,rgba(201,181,170,0) 70%),
      radial-gradient(ellipse 300px 380px at 1080px 300px,#5f7f9e 0%,rgba(95,127,158,0) 75%),
      linear-gradient(90deg,#dde9ee 0%,#e4ecef 40%,#a8bccc 70%,#7b97b3 100%)}
  .hero h1{position:absolute;left:52px;top:98px;font-weight:300;font-size:37px;
    line-height:59px;color:var(--ink);letter-spacing:.3px}
  .cta{position:absolute;left:52px;top:353px;width:353px;height:60px;background:var(--green);
    border-bottom:2px solid var(--green-dark);color:#fff;font-size:22px;display:flex;
    align-items:center;justify-content:center;gap:18px;letter-spacing:.3px}
  .hexes{position:absolute;left:0;top:-127px}
  .hex-label{font-family:"Roboto Condensed",sans-serif;font-weight:700;fill:#fff;text-anchor:middle}

  .welcome{position:absolute;left:54px;top:715px;width:722px}
  .welcome h2{font-weight:300;font-size:43px;color:var(--ink);line-height:1.1;margin-bottom:8px}
  .welcome h2 span{color:var(--blue-text)}
  .welcome p{font-size:14.3px;line-height:25.3px;color:var(--body)}
  .read-more{display:inline-block;margin-top:14px;width:141px;height:42px;background:var(--green);
    border-bottom:2px solid var(--green-dark);color:#fff;font-size:19px;line-height:40px;text-align:center}

  .vision{position:absolute;left:802px;top:727px;width:345px;height:333px;
    background:linear-gradient(160deg,#e6f2fc,var(--vision-bg));
    border-bottom:6px solid var(--vision-edge);border-radius:3px;text-align:center;padding:40px 20px 0}
  .vision h3{font-weight:400;font-size:30px;color:var(--blue-text);margin-bottom:6px}
  .vision p{font-size:14.5px;line-height:28px;color:#333;white-space:nowrap}

  .services{position:absolute;left:0;top:1142px;width:1200px;height:300px;
    background:linear-gradient(180deg,#e8f1f4,#f3f8fa)}
  .services h2{position:absolute;top:70px;width:100%;text-align:center;font-weight:300;font-size:43px;color:var(--ink)}
  .services h2 span{color:var(--blue-text)}
</style>
</head>
<body>
  <header class="site-header">
    <div class="brand">
      <span class="brand-mark"></span>
      <span class="brand-name">Brightmoor Systems Collective</span>
    </div>
    <div class="call">Call Us: <strong>555-014-(2290)</strong></div>
    <div class="social">
      <a class="first" href="#" aria-label="Social profile one"></a>
      <a class="second" href="#" aria-label="Social profile two"></a>
      <a class="third" href="#" aria-label="Social profile three"></a>
    </div>
    <nav class="nav">
      <a class="active" href="#" style="left:545px">Home</a>
      <a href="#" style="left:646px">About Us</a>
      <a href="#" style="left:769px">Our Services</a>
      <a href="#" style="left:914px">Our Benefits</a>
      <a href="#" style="left:1061px">Contact Us</a>
    </nav>
  </header>

  <section class="hero" role="img" aria-label="Photo of a hand touching a glowing technology interface with a businessman in the background">
    <h1>WE OFFER END TO END<br>TECHNOLOGY ADVISORY<br>SERVICES TO SMALL<br>BUSINESSES</h1>
    <a class="cta" href="#">GET STARTED NOW
      <svg width="20" height="16" viewBox="0 0 20 16"><path d="M2 2l6 6-6 6M10 2l6 6-6 6" fill="none" stroke="#fff" stroke-width="2.6"/></svg>
    </a>
    <svg class="hexes" width="1200" height="633" viewBox="0 0 1200 633">
      <defs>
        <polygon id="hex" points="-101,0 -50.5,-87 50.5,-87 101,0 50.5,87 -50.5,87"/>
      </defs>
      <g stroke="#8fb8df" stroke-width="1.2">
        <use href="#hex" x="638" y="281" fill="#2f7fd0" fill-opacity=".75"/>
        <use href="#hex" x="791" y="548" fill="#1e5c98" fill-opacity=".6"/>
        <use href="#hex" x="791" y="194" fill="var(--blue)"/>
        <use href="#hex" x="945" y="281" fill="var(--blue)"/>
        <use href="#hex" x="791" y="370" fill="var(--blue)"/>
        <use href="#hex" x="945" y="459" fill="var(--blue)"/>
      </g>
      <text class="hex-label" font-size="24"><tspan x="791" y="186">Virtualization</tspan><tspan x="791" y="219">Technologies</tspan></text>
      <text class="hex-label" font-size="33"><tspan x="638" y="270">IT</tspan><tspan x="638" y="313">Planning</tspan></text>
      <text class="hex-label" font-size="24"><tspan x="945" y="272">Server</tspan><tspan x="945" y="305">Infrastructure</tspan></text>
      <text class="hex-label" font-size="24"><tspan x="791" y="346">Business</tspan><tspan x="791" y="380">Continuity</tspan><tspan x="791" y="414">Planning</tspan></text>
      <text class="hex-label" font-size="24"><tspan x="945" y="450">Cloud</tspan><tspan x="945" y="483">Computing</tspan></text>
      <text class="hex-label" font-size="24"><tspan x="791" y="538">Project</tspan><tspan x="791" y="571">Management</tspan></text>
    </svg>
  </section>

  <section class="welcome">
    <h2>WELCOME TO <span>BSC GROUP</span></h2>
    <p>Lorem ipsum dolor sit amet, consectetur adipiscing elit. Donec venenatis vehicula rhoncus. Sspendisse ultricies posuere euismod. Quisque rutrum sollicitudin faucibus. Ut eu enim ac augue ultricies bibdum. Proin eget lectus diam, id feugiat ante. Nam lobortis magna sed est posuere eget ornare augue facilisis.<br>Cras nulla tellus, eleifend eu interdum at, pharetra ut felis. Donec semper, augue eu venenatis constur,<br>ipsum nisl placerat lorem, et eleifend enim odio vitae odio. Proin ac tortor malesuada lacus rhoncus<br>vehicula. Donec dui dolor, rutrum rutrum sagittis quis, mattis in nulla. Pellentesque elementum enim id<br>turpis consectetur laoreet. Vestibulum tempus condimentum lorem, quis bibendum mi eleifend eu.<br>Nullam eros ante, ultrices vitae malesuada sed, sollicitudin vitae tellus. Phasellus congue egestas nunc,<br>quis dapibus diam gravida a.</p>
    <a class="read-more" href="#">Read More</a>
  </section>

  <aside class="vision">
    <h3>OUR VISION</h3>
    <p>Lorem ipsum dolor sit amet, consectetur<br>adiscing elit. Donec venenatis vehicula<br>roncus. Sspendisse ultricies posuere euis-<br>mod. Quisque rutrum sollicitudin fauci-<br>bus. Ut eu enim ac augue ultricies<br>bibdum. Proin eget lectus diam, id feugiat<br>ante.</p>
  </aside>

  <section class="services">
    <h2>OUR <span>SERVICES</span></h2>
  </section>
</body>
</html>
```